Business Card Design Project

Hi Designers, this project is currently on hold until the Logo is completed:
Please submit to the Logo project here:
http://jobs.pixelmarket.example/job.aspx?id=371905

Once logo is completed, it will be attached to this project for you to create business cards with show logo, company name and address

Maren T K Ashdown

Corwin's Meadow Pine Flock Co.
Hazelmere
Upper Brackwell
North Devon EX21 4TN

Tel: 01809 351846
Mobile: 07912 463078
email: maren@meadow-pine-flock.example
Updates

Project Deadline Extended
Reason: Sorry everyone, we have had a sick ewe and I am now behind with this one and need to extend the deadline. Best wishes Maren

The designer who wins the logo brief will be asked to design the business card. Many thanks Maren

Project Deadline Extended
Reason: Sorry everyone, just a chaotic time of year with animals. Need to extend the deadline again..... as I just haven't had enough time to take a good look.... Thank you for your understanding. Maren

Project Deadline Extended
Reason: Sorry everyone It is our busiest time of year with animals and just no time to spend going through such great designs. I will have to extend the deadline again and hopefully have some news very soon. Wishing you all a very happy Christmas and a happy and healthy new year. Maren & Corwin

Target Market(s)

High end market
Boutique restaurants for meat (it's not commercial lamb it's a slow matured quality meat more like venison/beef) expensive - specialized market

High End shoot clothing / wool / sheepskin rugs
Quality products

Industry/Entity Type

Business

Requirements
Must have
• based on the logo - (which Pixel Market has just been asked to do)
possibly based on a simplified picture of a Hebridean Ram (shows it's a Hebridean by it's horns as opposed to other black sheep!!)

```html
<!DOCTYPE html>
<html lang="en">
<head>
<meta charset="utf-8">
<title>Corwin's Meadow Pine Flock Co. – Business Card</title>
<link rel="stylesheet" href="https://fonts.googleapis.com/css2?family=Tinos:wght@400;700&display=swap">
<style>
  :root {
    --page: #e9e7e4;
    --paper: #f6fbf9;
    --ink: #111111;
    --band: #140b0e;
    --green: #45c04a;
    --green-text: #e8f7e6;
    --faint: #d9ecdc;
  }
  * { margin: 0; padding: 0; box-sizing: border-box; }
  html, body {
    width: 1200px; height: 960px; overflow: hidden;
    background: var(--page);
    font-family: "Tinos", "Times New Roman", serif;
  }
  .canvas { position: relative; width: 1200px; height: 960px; }
  .card {
    position: absolute; left: 320px; width: 560px; height: 320px;
    background: var(--paper); overflow: hidden;
    box-shadow: 0 6px 18px rgba(0,0,0,.18);
  }
  .card--front { top: 110px; }
  .card--back { top: 530px; }

  /* front */
  .front-mark {
    position: absolute; left: 225px; top: 28px; width: 130px; height: 130px;
    border-radius: 50%; border: 10px solid var(--faint);
  }
  .front-band {
    position: absolute; left: 0; right: 0; top: 178px; height: 86px;
    background: var(--band); display: flex; align-items: center; justify-content: center;
  }
  .front-stripe {
    position: absolute; left: 0; right: 0; top: 272px; bottom: 0; background: var(--green);
  }

  .brand { color: currentColor; text-transform: uppercase; font-weight: 400; line-height: 1; }
  .brand__name { display: block; font-size: 30px; letter-spacing: 2px; }
  .brand__sub { display: block; font-size: 9.5px; letter-spacing: 2.4px; margin-top: 3px; }
  .front-band .brand { color: #f2f2f2; }

  /* back */
  .contact-list {
    position: absolute; left: 46px; top: 34px; list-style: none;
    color: var(--ink); font-size: 19px;
  }
  .contact-list li { display: flex; align-items: center; gap: 18px; height: 33px; }
  .contact-list svg { width: 15px; height: 15px; fill: var(--ink); flex: none; }
  .back-rule {
    position: absolute; left: 0; right: 0; top: 178px; height: 12px; background: #0d1a0e;
  }
  .back-panel {
    position: absolute; left: 0; right: 0; top: 196px; bottom: 0; background: var(--green);
  }
  .back-logo {
    position: absolute; left: 34px; top: 240px; display: flex; align-items: center; gap: 14px;
    color: var(--ink);
  }
  .back-logo__circle {
    width: 56px; height: 56px; border-radius: 50%; border: 5px solid var(--ink);
  }
  .holder-name {
    position: absolute; right: 36px; top: 212px;
    color: var(--green-text); font-size: 22px;
  }
</style>
</head>
<body>
<main class="canvas">

  <section class="card card--front" aria-label="Card front">
    <div class="front-mark" aria-hidden="true"></div>
    <div class="front-band">
      <span class="brand">
        <span class="brand__name">Corwin's</span>
        <span class="brand__sub">Meadow Pine Flock Co.</span>
      </span>
    </div>
    <div class="front-stripe"></div>
  </section>

  <section class="card card--back" aria-label="Card back">
    <ul class="contact-list">
      <li>
        <svg viewBox="0 0 16 16"><path d="M8 1a5 5 0 0 0-5 5c0 4 5 9 5 9s5-5 5-9a5 5 0 0 0-5-5zm0 7a2 2 0 1 1 0-4 2 2 0 0 1 0 4z"/></svg>
        Hazelmere Upper Brackwell North Devon EX21 4TN
      </li>
      <li>
        <svg viewBox="0 0 16 16"><path d="M2 5c0-2 3-3 6-3s6 1 6 3v1h-3V5H5v1H2zM4 7h8l2 7H2zm4 1.5a2 2 0 1 0 0 4 2 2 0 0 0 0-4z"/></svg>
        01809 351846
      </li>
      <li>
        <svg viewBox="0 0 16 16"><path d="M5 1h6a1 1 0 0 1 1 1v12a1 1 0 0 1-1 1H5a1 1 0 0 1-1-1V2a1 1 0 0 1 1-1zm0 2v7h6V3zm1 8v2h4v-2z"/></svg>
        07912 463078
      </li>
      <li>
        <svg viewBox="0 0 16 16"><path d="M1 3h14v10H1zm1.5 1.2L8 8.5l5.5-4.3z"/></svg>
        maren@meadow-pine-flock.example
      </li>
    </ul>
    <div class="back-rule"></div>
    <div class="back-panel"></div>
    <div class="back-logo">
      <span class="back-logo__circle" aria-hidden="true"></span>
      <span class="brand">
        <span class="brand__name">Corwin's</span>
        <span class="brand__sub">Meadow Pine Flock Co.</span>
      </span>
    </div>
    <p class="holder-name">Maren T K Ashdown</p>
  </section>

</main>
</body>
</html>
```